Pin Oak Media Outdoor Advertising Corporate Stationery Design

We need a full corporate stationary design for our company Pin Oak Media. We setup and lease billboards, building wraps, trailer ads and construction hoardings.

We need to establish our branding and our newly created logo. All our brand identity should point towards our values, vision and mission.

We are open to fresh new ideas for our stationary design as long as it ultimately reflects the brand & logo.

Corporate Stationary List:
1. Business Card Design
2. Letterhead Design
3. Email Signature Design
4. “Advertise Here” Design (for placement on empty billboards, etc)

All designs must include our logo and be kept simple, modern, friendly and effective.

All designs should please be provided in Illustrator, Photoshop and InDesign file formats.

More details are attached in Word.

Hey

The project has been guaranteed. We like what has been submitted so far but we''d like to see a few concepts for the "Advertise Here" design for open billboards please.

Thanks!

Target Market(s)

Male and female, corporates, business owners, media buying agencies, government & all age groups.

Industry/Entity Type

Construction

Requirements
Must have
• All designs must incorporate our colours: Pantone 319C, 320C, 321C & Hexachrome Black C.

1.Business Card Design
a. Logo
b. Name
c. Mobile
d. Landline
e. Website
f. Facebook
g. Twitter
2. Letterhead Design
a. Logo
b. Mobile
c. Landline
d. Website
e. CC reg number
f. BEE level 4 contributor
g. PRTVA member
h. Postal Address
3. Email Signature Design
a. Logo
b. Name
c. Mobile
d. Landline
e. BEE level 4 contributor
f. PRTVA member
g. Website
h. Facebook
i. Twitter
4. “Advertise Here” Design (for placement on empty billboards, etc) Majority ratio of 2:1 (eg 6m wide by 3m high) - Please use 2 attached photos.
a. Logo .co.za
b. Contact Mirela
c. Mobile
Nice to have
• Come up with a cool slogan / tagline for Business Cards, “Advertise Here” Design

```html
<!DOCTYPE html>
<html lang="en">
<head>
<meta charset="utf-8">
<title>Pin Oak Media — Corporate Stationery</title>
<link rel="stylesheet" href="https://fonts.googleapis.com/css2?family=Arimo:wght@400;700&display=swap">
<style>
  :root{
    --teal-dark:#0b8b95;
    --teal-mid:#2ea7ae;
    --teal-light:#6fcdd3;
    --ink:#1b1b1b;
    --paper:#ffffff;
    --paper-shade:#eceded;
    --backdrop:#3b3c3e;
    --muted:#8fbfc2;
  }
  *{box-sizing:border-box;margin:0;padding:0}
  html,body{width:1200px;height:960px;overflow:hidden}
  body{background:var(--backdrop);font-family:"Arimo",Arial,sans-serif;color:var(--ink);position:relative}

  .sheet{position:absolute;background:linear-gradient(180deg,var(--paper-shade) 0%,var(--paper) 30%,var(--paper) 70%,#f3f4f4 100%);overflow:hidden}

  .band{position:absolute;left:0;right:0;bottom:0;height:20px;background:var(--teal-dark)}
  .band-accent{position:absolute;right:0;bottom:0;background:var(--teal-light);clip-path:polygon(7% 0,100% 0,100% 100%,0 100%)}

  .brand{display:flex;align-items:center;gap:8px;white-space:nowrap}
  .brand-square{background:var(--teal-mid);flex:none}
  .brand-name{font-weight:700;color:var(--ink);letter-spacing:-0.5px}

  .contact-list{list-style:none}
  .contact-list li{display:flex;align-items:center;gap:6px;color:#333}
  .contact-list svg{fill:var(--teal-mid);flex:none}

  /* Letterhead */
  .letterhead{left:77px;top:79px;width:568px;height:800px}
  .letterhead .brand{position:absolute;left:59px;top:44px}
  .letterhead .brand-square{width:30px;height:30px}
  .letterhead .brand-name{font-size:25px}
  .letterhead .contact-list{position:absolute;left:328px;top:42px}
  .letterhead .contact-list li{font-size:9.5px;line-height:14px}
  .letterhead .contact-list li.phone{font-size:11px}
  .letterhead-watermark{position:absolute;left:20px;top:540px;width:320px;height:320px;border-radius:50%;background:#e4eced;opacity:.7}
  .letterhead-url{position:absolute;left:53px;bottom:28px;font-size:12px;letter-spacing:3.6px;color:#333}
  .letterhead .band{height:20px}
  .letterhead .band-accent{width:212px;height:31px}

  /* Billboard face */
  .billboard{left:661px;top:79px;width:461px;height:230px;background:var(--paper);border:6px solid #1d1d1d}
  .billboard-headline{position:absolute;left:22px;top:16px;font-weight:700;font-size:60px;line-height:52px;letter-spacing:-1px;color:var(--teal-dark);text-transform:uppercase}
  .billboard-headline .light{color:var(--teal-light)}
  .billboard .brand{position:absolute;left:300px;top:70px;gap:5px}
  .billboard .brand-square{width:14px;height:14px}
  .billboard .brand-name{font-size:13px}
  .billboard-contact{position:absolute;left:300px;top:100px;font-size:10px;line-height:13px;color:#222}
  .billboard-contact .phone{font-size:11px}
  .billboard .band{height:12px}
  .billboard .band-accent{width:160px;height:18px}

  /* Business card front */
  .card-front{left:661px;top:338px;width:461px;height:262px}
  .card-front .brand{position:absolute;left:52px;top:96px;gap:10px}
  .card-front .brand-square{width:40px;height:40px}
  .card-front .brand-name{font-size:38px}
  .card-front-url{position:absolute;left:170px;top:148px;font-size:11.5px;letter-spacing:1.6px;color:#222}
  .card-front .band{height:14px}
  .card-front .band-accent{width:146px;height:24px}

  /* Business card back */
  .card-back{left:661px;top:618px;width:461px;height:262px}
  .card-back .brand{position:absolute;left:30px;top:46px}
  .card-back .brand-square{width:22px;height:22px}
  .card-back .brand-name{font-size:22px}
  .card-holder{position:absolute;right:32px;top:84px;text-align:right}
  .card-holder-name{font-size:17px;color:var(--ink)}
  .card-holder-role{font-size:11px;color:var(--teal-mid)}
  .card-back .contact-list{position:absolute;left:28px;top:150px}
  .card-back .contact-list li{font-size:11px;line-height:16px}
  .card-back .contact-list li.phone{font-size:14px;line-height:20px}
  .card-back .band{height:14px}
  .card-back .band-accent{width:146px;height:24px}
</style>
</head>
<body>

<section class="sheet letterhead" aria-label="Letterhead">
  <div class="brand"><span class="brand-square"></span><span class="brand-name">Pin Oak Media</span></div>
  <ul class="contact-list">
    <li><svg width="8" height="9" viewBox="0 0 10 10"><path d="M5 0C3 0 1.5 1.5 1.5 3.4 1.5 6 5 10 5 10s3.5-4 3.5-6.6C8.5 1.5 7 0 5 0z"/></svg>2240 Larkspur Lane, Fernhill, FL 34710</li>
    <li class="phone"><svg width="6" height="9" viewBox="0 0 6 10"><rect width="6" height="10" rx="1"/></svg>400 555 2468</li>
    <li><svg width="9" height="7" viewBox="0 0 10 7"><path d="M0 0h10v7H0z"/></svg>hello@pinoakmedia.com</li>
  </ul>
  <div class="letterhead-watermark" aria-hidden="true"></div>
  <p class="letterhead-url">www.pinoakmedia.com</p>
  <div class="band"></div>
  <div class="band-accent"></div>
</section>

<section class="sheet billboard" aria-label="Advertise here billboard">
  <h1 class="billboard-headline">“Adver<br>tise<br><span class="light">Here”</span></h1>
  <div class="brand"><span class="brand-square"></span><span class="brand-name">Pin Oak Media</span></div>
  <div class="billboard-contact">
    <p class="phone">400 555 2468</p>
    <p>hello@pinoakmedia.com</p>
    <p>www.pinoakmedia.com</p>
  </div>
  <div class="band"></div>
  <div class="band-accent"></div>
</section>

<section class="sheet card-front" aria-label="Business card front">
  <div class="brand"><span class="brand-square"></span><span class="brand-name">Pin Oak Media</span></div>
  <p class="card-front-url">www.pinoakmedia.com</p>
  <div class="band"></div>
  <div class="band-accent"></div>
</section>

<section class="sheet card-back" aria-label="Business card back">
  <div class="brand"><span class="brand-square"></span><span class="brand-name">Pin Oak Media</span></div>
  <div class="card-holder">
    <p class="card-holder-name">Dan Mercer</p>
    <p class="card-holder-role">Manager</p>
  </div>
  <ul class="contact-list">
    <li><svg width="10" height="11" viewBox="0 0 10 10"><path d="M5 0C3 0 1.5 1.5 1.5 3.4 1.5 6 5 10 5 10s3.5-4 3.5-6.6C8.5 1.5 7 0 5 0z"/></svg>2240 Larkspur Lane, Fernhill, FL 34710</li>
    <li class="phone"><svg width="8" height="12" viewBox="0 0 6 10"><rect width="6" height="10" rx="1"/></svg>400 555 2468</li>
    <li><svg width="10" height="8" viewBox="0 0 10 7"><path d="M0 0h10v7H0z"/></svg>hello@pinoakmedia.com</li>
    <li><svg width="10" height="10" viewBox="0 0 10 10"><circle cx="5" cy="5" r="5"/></svg>www.pinoakmedia.com</li>
  </ul>
  <div class="band"></div>
  <div class="band-accent"></div>
</section>

</body>
</html>
```